New business stationairy

I need paper with header and footer and business cards.
I am a Ltd Company and my main field of expertise is QA/QC inspection in the Oil and Gas Industry. I will need all contact detail inserted and a footer with registration number and bank details etc

Industry/Entity Type

Business

```html
<!DOCTYPE html>
<html lang="en">
<head>
<meta charset="utf-8">
<title>Halden Inspection Services Ltd – Stationery</title>
<link rel="stylesheet" href="https://fonts.googleapis.com/css2?family=EB+Garamond:wght@400;500&family=Roboto+Condensed:wght@400;700&display=swap">
<style>
  :root {
    --stage: #1f4fd6;
    --paper: #f7f7f8;
    --navy: #1e2c78;
    --blue: #1f8fd0;
    --ink: #1c2350;
    --faint: #e6e6e8;
  }
  * { box-sizing: border-box; margin: 0; padding: 0; }
  html, body { width: 1200px; height: 987px; overflow: hidden; }
  body {
    background: var(--stage);
    position: relative;
    font-family: "EB Garamond", Georgia, serif;
  }

  /* Letterhead */
  .letterhead {
    position: absolute; left: 90px; top: 95px;
    width: 560px; height: 792px;
    background: var(--paper);
    overflow: hidden;
  }
  .brand { display: flex; align-items: center; gap: 10px; }
  .brand-dot { width: 30px; height: 30px; border-radius: 50%; background: var(--blue); flex: none; }
  .brand-name {
    font-family: "EB Garamond", Georgia, serif;
    font-weight: 400; color: var(--navy);
    line-height: 1.05;
  }
  .letterhead .brand { position: absolute; left: 44px; top: 44px; }
  .letterhead .brand-name { font-size: 22px; }
  .backdrop-circle {
    position: absolute; left: 190px; top: 230px;
    width: 330px; height: 330px; border-radius: 50%;
    border: 26px solid var(--faint);
  }
  .footer-details {
    position: absolute; right: 40px; bottom: 66px;
    text-align: right; font-size: 11.5px; line-height: 1.5;
    color: var(--blue);
  }
  .footer-details .strong { color: var(--navy); }
  .footer-band { position: absolute; left: 0; bottom: 0; width: 100%; height: 60px; }

  /* Business cards */
  .card {
    position: absolute; width: 340px; height: 196px; overflow: hidden;
  }
  .card-front { left: 770px; top: 690px; background: var(--navy); }
  .card-front .brand { position: absolute; left: 44px; top: 74px; }
  .card-front .brand-name { color: #fff; font-size: 21px; }

  .card-back { left: 770px; top: 440px; background: var(--paper); }
  .card-back .brand { position: absolute; right: 22px; top: 20px; }
  .card-back .brand-dot { width: 22px; height: 22px; }
  .card-back .brand-name { font-size: 15px; }
  .holder { position: absolute; left: 26px; top: 60px; font-family: "Roboto Condensed", Arial, sans-serif; }
  .holder-name { font-weight: 700; font-size: 16px; color: var(--ink); }
  .holder-role { font-size: 11px; color: var(--blue); margin-top: 2px; }
  .contact-list {
    position: absolute; left: 26px; top: 118px; list-style: none;
    font-family: "Roboto Condensed", Arial, sans-serif; font-size: 9.5px; color: var(--ink);
  }
  .contact-list li { display: flex; align-items: flex-start; gap: 6px; margin-bottom: 3px; line-height: 1.25; }
  .contact-list svg { width: 10px; height: 10px; flex: none; fill: var(--navy); margin-top: 1px; }
  .card-band { position: absolute; left: 0; bottom: 0; width: 100%; height: 80px; }
</style>
</head>
<body>

<section class="letterhead" aria-label="Letterhead">
  <div class="brand">
    <span class="brand-dot"></span>
    <span class="brand-name">Halden Inspection<br>Services Ltd</span>
  </div>
  <div class="backdrop-circle" aria-hidden="true"></div>
  <div class="footer-details">
    <p>Add. Elm Cottage Mill Road Ashby Vale Dorset DT0 0AA</p>
    <p>Ph. 01632 960418, Email. morgan.reid@example.co.uk</p>
    <p class="strong">Vat No. # 00000000 Bank No. # 1111111111 Reg. No. # 1122334455</p>
  </div>
  <svg class="footer-band" viewBox="0 0 560 60" preserveAspectRatio="none" aria-hidden="true">
    <path d="M0 60 L0 46 Q300 40 560 0 L560 60 Z" fill="var(--blue)"/>
    <path d="M0 60 L0 52 Q300 48 560 12 L560 60 Z" fill="var(--navy)"/>
  </svg>
</section>

<section class="card card-back" aria-label="Business card, contact side">
  <div class="brand">
    <span class="brand-dot"></span>
    <span class="brand-name">Halden Inspection<br>Services Ltd</span>
  </div>
  <div class="holder">
    <p class="holder-name">Morgan Reid</p>
    <p class="holder-role">Owner</p>
  </div>
  <ul class="contact-list">
    <li><svg viewBox="0 0 10 10"><path d="M2 0.5 L3.6 2.6 L2.8 3.6 Q4 6 6.4 7.2 L7.4 6.4 L9.5 8 L8.4 9.5 Q2 8.6 0.5 1.6 Z"/></svg>01632 960418</li>
    <li><svg viewBox="0 0 10 10"><path d="M0.5 2 H9.5 V8.5 H0.5 Z M1 2.4 L5 5.6 L9 2.4" stroke="#fff" stroke-width="0.8"/></svg>morgan.reid@example.co.uk</li>
    <li><svg viewBox="0 0 10 10"><path d="M5 0.5 A3.2 3.2 0 0 1 8.2 3.7 Q8.2 6 5 9.5 Q1.8 6 1.8 3.7 A3.2 3.2 0 0 1 5 0.5 Z"/></svg>Elm Cottage Mill Road Ashby Vale<br>Dorset DT0 0AA</li>
  </ul>
  <svg class="card-band" viewBox="0 0 340 80" preserveAspectRatio="none" aria-hidden="true">
    <path d="M150 80 Q260 60 340 0 L340 80 Z" fill="var(--blue)"/>
    <path d="M140 80 Q260 66 340 14 L340 80 Z" fill="var(--navy)"/>
  </svg>
</section>

<section class="card card-front" aria-label="Business card, front">
  <div class="brand">
    <span class="brand-dot"></span>
    <span class="brand-name">Halden Inspection<br>Services Ltd</span>
  </div>
</section>

</body>
</html>
```